Belmora - Medical Device Company Needs Box Refined

We are a medical device company needing our packaging refined. This she be clean and sophisticated. The logo must not be change. Please see the attached sample for baseline and sizing.

It Company

```html
<!DOCTYPE html>
<html lang="en">
<head>
<meta charset="utf-8">
<title>Belmora Intraocular Lens Box – Dieline</title>
<link rel="stylesheet" href="https://fonts.googleapis.com/css2?family=Arimo:wght@400;700&family=Open+Sans:ital,wght@0,400;0,700;1,400&display=swap">
<style>
  :root {
    --spot-blue: #0a72b8;
    --spot-cyan: #29abe2;
    --spot-yellow: #fff200;
    --spot-black: #1a1a1a;
    --dieline: #4f9c8c;
    --paper: #ffffff;
    --ink: #1a1a1a;
  }
  html, body { margin: 0; padding: 0; overflow: hidden; background: var(--paper); }
  .sheet { display: block; width: 960px; height: 1200px; }
  .cut { fill: none; stroke: var(--dieline); stroke-width: 1; }
  .fold { fill: none; stroke: var(--dieline); stroke-width: 1; stroke-dasharray: 5 4; }
  .reg-mark { fill: none; stroke: var(--dieline); stroke-width: 1; }
  .brand-name { font-family: "Arimo", sans-serif; font-weight: 400; fill: var(--spot-blue); }
  .brand-dot { fill: var(--spot-yellow); }
  .product-line { font-family: "Arimo", sans-serif; fill: var(--ink); }
  .body-text { font-family: "Arimo", sans-serif; fill: var(--ink); font-size: 8.5px; }
  .body-bold { font-family: "Arimo", sans-serif; font-weight: 700; fill: var(--ink); }
  .icon { fill: none; stroke: var(--ink); stroke-width: 0.8; }
  .barcode-frame { fill: none; stroke: var(--ink); stroke-width: 1.2; stroke-dasharray: 6 4; }
  .ref-band { fill: var(--spot-black); }
  .ref-label { font-family: "Arimo", sans-serif; font-weight: 700; font-size: 11px; fill: #fff; letter-spacing: 1px; }
  .spec-frame { fill: none; stroke: var(--ink); stroke-width: 1; }
  .spec-head { fill: var(--spot-black); }
  .spec-head-text { font-family: "Open Sans", sans-serif; font-weight: 700; font-size: 11px; fill: #fff; }
  .spec-cell { font-family: "Open Sans", sans-serif; font-size: 11px; fill: var(--ink); }
  .spec-note { font-family: "Open Sans", sans-serif; font-size: 12px; fill: var(--ink); }
  .spec-note-strong { font-weight: 700; }
  .spec-note-em { font-style: italic; }
  .spec-rule { stroke: var(--ink); stroke-width: 1; }
  .swatch-label { font-family: "Open Sans", sans-serif; font-size: 9px; }
  .brief-caption { font-family: "Open Sans", sans-serif; font-weight: 700; font-size: 13px; fill: var(--ink); }
  .small-print { font-family: "Arimo", sans-serif; font-size: 8px; fill: var(--ink); }
</style>
</head>
<body>
<svg class="sheet" viewBox="0 0 928 1163" preserveAspectRatio="none" xmlns="http://www.w3.org/2000/svg">
  <defs>
    <linearGradient id="eyeTone" x1="0" y1="0" x2="1" y2="1">
      <stop offset="0" stop-color="#7cc6ee"/>
      <stop offset="1" stop-color="#0a72b8"/>
    </linearGradient>
    <radialGradient id="lensTone" cx="0.5" cy="0.5" r="0.5">
      <stop offset="0" stop-color="#f3f9fd"/>
      <stop offset="1" stop-color="#c5dff1"/>
    </radialGradient>
  </defs>

  <g class="reg-marks">
    <g class="reg-mark"><circle cx="50" cy="82" r="16"/><path d="M50 60V104M28 82H72"/></g>
    <g class="reg-mark"><circle cx="878" cy="82" r="16"/><path d="M878 60V104M856 82H900"/></g>
    <g class="reg-mark"><circle cx="50" cy="800" r="16"/><path d="M50 778V822M28 800H72"/></g>
    <g class="reg-mark"><circle cx="878" cy="800" r="16"/><path d="M878 778V822M856 800H900"/></g>
    <path class="reg-mark" d="M30 0V40M905 0V40M230 0V14M700 0V14M30 1018V1042M905 1018V1042"/>
  </g>

  <g class="dieline">
    <path class="cut" d="M115 160V58Q115 50 123 48L228 22H702L807 48Q815 50 815 58V160"/>
    <path class="cut" d="M230 163L60 165Q30 166 30 195V465Q30 495 60 495L230 497"/>
    <path class="cut" d="M700 163L875 165Q905 166 905 195V465Q905 495 875 495L700 497"/>
    <path class="cut" d="M230 497L115 510V610Q115 620 125 620L230 625"/>
    <path class="cut" d="M700 497L813 510V610Q813 620 803 620L700 625"/>
    <path class="cut" d="M230 625V962M700 625V962"/>
    <path class="cut" d="M230 962V1008H700V962"/>
    <path class="fold" d="M230 22V160M700 22V160M230 160H700M230 497H700M230 625H700M230 962H700"/>
    <path class="fold" d="M100 170V490M828 170V490M230 160V625M700 160V625"/>
  </g>

  <g class="top-flap" transform="rotate(180 465 80)">
    <text class="small-print" x="355" y="50">Northvale Optics Ltd.</text>
    <text class="small-print" x="355" y="62">Harrow House, Linden Road, Kestford, Westshire</text>
    <text class="small-print" x="355" y="74">KT 4 9PQ, United Kingdom</text>
    <text class="small-print" x="355" y="86">Website: www.nvo-optics.com&#160;&#160;&#160;E-mail: info@nvo-optics.com</text>
    <text class="small-print" x="490" y="108" font-size="6">REV.06 NVO03062015</text>
  </g>

  <g class="front-panel">
    <circle class="brand-dot" cx="274" cy="214" r="8"/>
    <text class="brand-name" x="286" y="223" font-size="22">Belmora</text>
    <text class="product-line" x="368" y="226" font-size="12.5">HYDROPHILIC ACRYLIC INTRAOCULAR LENS</text>
    <rect x="232" y="300" width="396" height="142" rx="70" fill="url(#eyeTone)" role="img" aria-label="Stylised blue eye illustration"/>
    <text class="body-text" x="502" y="459" font-size="8">CONTENTS:</text>
    <text class="body-bold" x="502" y="470" font-size="11" letter-spacing="1">ONE INTRAOCULAR LENS</text>
  </g>

  <g class="side-flap-right">
    <text class="body-text" font-size="5.5" transform="translate(818 198) rotate(90)">Single</text>
    <text class="body-text" font-size="5.5" transform="translate(810 198) rotate(90)">Use Only</text>
    <g class="icon"><circle cx="812" cy="248" r="5.5"/><path d="M808 244L816 252"/></g>
    <g class="icon"><circle cx="812" cy="278" r="5.5"/><path d="M808 282L816 274"/></g>
    <g class="icon"><path d="M812 302L818 313H806Z"/></g>
    <g class="icon"><rect x="806" y="328" width="12" height="28"/></g>
    <g transform="translate(735 440) rotate(-90)">
      <circle class="brand-dot" cx="-22" cy="-8" r="6"/>
      <text class="brand-name" x="-14" y="4" font-size="14">Belmora</text>
    </g>
  </g>

  <g class="side-panel">
    <text class="body-text" x="138" y="567" font-size="8.5">90 x 35 x 128mm</text>
    <circle class="brand-dot" cx="263" cy="549" r="7"/>
    <text class="brand-name" x="273" y="558" font-size="18">Belmora</text>
    <text class="product-line" x="258" y="590" font-size="12">HYDROPHILIC ACRYLIC INTRAOCULAR LENS</text>
    <ellipse cx="620" cy="567" rx="62" ry="36" fill="url(#lensTone)" role="img" aria-label="Intraocular lens with haptics"/>
    <circle cx="744" cy="544" r="10" fill="var(--spot-black)"/>
    <circle cx="781" cy="544" r="10" fill="var(--spot-yellow)"/>
    <circle cx="744" cy="580" r="10" fill="var(--spot-cyan)"/>
    <circle cx="781" cy="580" r="10" fill="var(--spot-blue)"/>
  </g>

  <g class="back-panel">
    <circle class="brand-dot" cx="437" cy="705" r="9"/>
    <text class="brand-name" x="450" y="720" font-size="22">Belmora</text>

    <g class="icon"><rect x="428" y="766" width="24" height="13"/><path d="M440 766V779"/></g>
    <text class="body-bold" x="462" y="776" font-size="12">Contains:</text>
    <text class="body-text" x="462" y="787">One sterile hydrophilic foldable aspheric intraocular lens</text>
    <text class="body-text" x="462" y="796">Patient ID Card, Product inserts</text>

    <g class="icon"><circle cx="441" cy="810" r="6"/><path d="M437 806L445 814"/></g>
    <text class="body-text" x="462" y="813">Do not use if the packaging is opened or damaged.</text>

    <g class="icon"><circle cx="441" cy="829" r="6"/><path d="M437 833L445 825"/></g>
    <text class="body-text" x="462" y="832">Do not resterile by any method.</text>

    <g class="icon"><path d="M437 842H445L441 850Z"/><path d="M441 850V853"/></g>
    <text class="body-text" x="462" y="850">Should not use after the specified month and year</text>

    <g class="icon"><path d="M441 864L448 876H434Z"/><path d="M441 868V872"/></g>
    <text class="body-text" x="462" y="869">Attention! see instruction for use</text>
    <text class="body-text" x="462" y="879">Store in cool and dry place.</text>

    <g class="icon"><circle cx="441" cy="893" r="6"/></g>
    <text class="body-text" x="438.5" y="896" font-size="8">2</text>
    <text class="body-text" x="462" y="896">FOR SINGLE USE ONLY</text>

    <g class="icon"><rect x="402" y="907" width="54" height="11"/><path d="M446 907V918"/></g>
    <text class="body-text" x="406" y="915" font-size="6">STERILE</text>
    <text class="body-text" x="462" y="916">Intraocular lens sterilized by steam.</text>

    <rect class="barcode-frame" x="252" y="796" width="110" height="152"/>
    <rect class="ref-band" x="296" y="806" width="22" height="104"/>
    <text class="ref-label" transform="translate(312 903) rotate(-90)">REFERENCE</text>
  </g>

  <g class="spec-table">
    <path class="spec-frame" d="M100 1038H835V1115H100Q85 1115 85 1100V1053Q85 1038 100 1038Z"/>
    <rect class="spec-head" x="205" y="1038" width="630" height="19"/>
    <path class="spec-rule" d="M205 1038V1080M205 1080H835M205 1057H835M445 1038V1080M610 1038V1080"/>
    <text class="spec-head-text" x="325" y="1052" text-anchor="middle">PACKING DESCRIPTION</text>
    <text class="spec-head-text" x="527" y="1052" text-anchor="middle">SIZE DIMENSIONS (mm)</text>
    <text class="spec-head-text" x="722" y="1052" text-anchor="middle">PANTONE COLORS</text>
    <text class="spec-cell" x="325" y="1073" text-anchor="middle">Hydrophilic Acrylic Intraocular Lens</text>
    <text class="spec-cell" x="527" y="1073" text-anchor="middle">90 x 35 x 128 mm</text>
    <rect x="620" y="1063" width="14" height="11" fill="var(--spot-blue)"/>
    <text class="swatch-label" x="638" y="1072" fill="var(--spot-blue)">3005</text>
    <rect x="667" y="1063" width="14" height="11" fill="var(--spot-cyan)"/>
    <text class="swatch-label" x="685" y="1072" fill="var(--spot-cyan)">CYAN</text>
    <rect x="720" y="1063" width="14" height="11" fill="var(--spot-yellow)"/>
    <text class="swatch-label" x="738" y="1072" fill="#e0c800">YELLOW</text>
    <rect x="783" y="1063" width="14" height="11" fill="var(--spot-black)"/>
    <text class="swatch-label" x="800" y="1072" fill="var(--ink)">BLACK</text>
    <text class="spec-note" x="222" y="1102"><tspan class="spec-note-strong">Note:</tspan> This box is made to print spot colors (4). <tspan class="spec-note-em">(Lens image high resolution in a single spot color)</tspan></text>
    <circle class="brand-dot" cx="110" cy="1066" r="8"/>
    <text class="brand-name" x="121" y="1075" font-size="19">Belmora</text>
    <text class="small-print" x="98" y="1109" font-size="7.5">Northvale Optics Ltd.</text>
  </g>

  <text class="brief-caption" x="464" y="1152" text-anchor="middle">Final art box 4 colors, just missing bar code information or anything else you need to include in the package</text>
</svg>
</body>
</html>
```